Minimalistic and chic product labels required for tea packaging

We need a Label Sticker Design for our tea company that is minimalistic, simple and chic.

We have 2 categories of tea: artisan tea (single flavoured tea e.g. green and black) and herbal teas (e.g. mixuture of herbs and flowers). We would like to have the designs to tell the difference of artisan tea and herbal tea, this can be done by having different colours to tell the difference or if there are other design features used.

We would also like to have colourful colours on our herbal tea range, preferably either a light and chic pastel colour palette or bright and chic colour palette.

The labels will be stuck onto a white pouch. The final design should also include the variety of colour palettes that can be used in AI format with the label. Preferred label measurements in 9cm width, and 11cm height. Our logo is attached.

Target Market(s)

Beauty and wellness

Industry/Entity Type

Health And Wellness

Requirements
Must have
• 2 x labels (front and back)
Front label must include logo, text to include tea type and weight
Back label must include text space to write description
Nice to have
• Simple and chic label design to stick onto a white pouch
Should not have
• Must not have too much graphic and pictures

```html
<!DOCTYPE html>
<html lang="en">
<head>
<meta charset="utf-8">
<title>Verdelle Tea Labels</title>
<link href="https://fonts.googleapis.com/css2?family=Montserrat:wght@300;400&display=swap" rel="stylesheet">
<style>
  :root {
    --bg: #dcdcdc;
    --label: #ffffff;
    --label-edge: #8d8d8d;
    --ink: #4a4a4a;
    --ink-soft: #6d6d6d;
    --tagline: #ffffff;
    --hill-back: #e6e6e6;
    --hill-herbal-a: #d7aaa5;
    --hill-herbal-b: #ecd3cf;
    --hill-green: #a4ad a2;
    --hill-green-a: #9ea89c;
    --hill-green-b: #c9d0c7;
    --hill-black-a: #4d4d4d;
    --hill-black-b: #8a8a8a;
    --tag-bg: #f4f4f4;
    --tag-edge: #b5b5b5;
  }
  * { box-sizing: border-box; margin: 0; padding: 0; }
  html, body { width: 1200px; height: 800px; overflow: hidden; }
  body {
    background: var(--bg);
    font-family: "Montserrat", sans-serif;
    color: var(--ink);
    position: relative;
  }
  .brand-header {
    position: absolute;
    right: 170px;
    top: 230px;
    text-align: right;
  }
  .brand-name {
    font-size: 34px;
    font-weight: 300;
    letter-spacing: 4px;
    color: var(--ink);
    margin-right: 10px;
  }
  .tagline {
    margin-top: 28px;
    font-size: 16px;
    font-weight: 300;
    letter-spacing: 1px;
    color: var(--tagline);
  }
  .label-row {
    position: absolute;
    left: 95px;
    top: 470px;
    display: flex;
    gap: 70px;
  }
  .label {
    position: relative;
    width: 200px;
    height: 244px;
    background: var(--label);
    border: 1px solid var(--label-edge);
    overflow: hidden;
  }
  .label-name {
    position: absolute;
    top: 26px;
    right: 14px;
    font-size: 9px;
    font-weight: 400;
    letter-spacing: 1.5px;
    color: var(--ink);
  }
  .hill {
    position: absolute;
    left: 0;
    bottom: 0;
    width: 200px;
    height: 90px;
  }
  .tea-tag {
    position: absolute;
    left: 50%;
    bottom: 40px;
    transform: translateX(-50%);
    background: var(--tag-bg);
    border: 1px solid var(--tag-edge);
    font-size: 6px;
    padding: 2px 8px;
    white-space: nowrap;
    color: var(--ink);
  }
  .tea-weight {
    position: absolute;
    left: 50%;
    bottom: 28px;
    transform: translateX(-50%);
    font-size: 4px;
    color: var(--ink-soft);
  }
  .back-copy {
    position: absolute;
    top: 26px;
    left: 26px;
    right: 36px;
    font-size: 4.5px;
    line-height: 1.45;
    color: var(--ink);
  }
  .back-copy p + p { margin-top: 5px; }
</style>
</head>
<body>
  <header class="brand-header">
    <div class="brand-name">Verdelle</div>
    <p class="tagline">Minimalistic and chic product labels required for tea packaging</p>
  </header>

  <main class="label-row">
    <section class="label label--back">
      <div class="back-copy">
        <p>A label for a small tea house that is calm, simple and light.</p>
        <p>Each pouch holds loose leaf tea picked with care. Artisan blends and herbal mixes sit side by side, marked by soft colour so each one is easy to tell apart.</p>
        <p>Steep in hot water for three to five minutes and enjoy.</p>
      </div>
      <svg class="hill" viewBox="0 0 200 90" role="img" aria-label="Faint striped hill illustration">
        <path d="M8 90 C40 40 90 20 120 30 C150 40 170 60 185 90 Z" fill="var(--hill-back)"/>
      </svg>
    </section>

    <section class="label label--herbal">
      <div class="label-name">Verdelle</div>
      <svg class="hill" viewBox="0 0 200 90" role="img" aria-label="Pastel pink striped hill illustration">
        <defs>
          <linearGradient id="herbal-fill" x1="0" x2="1">
            <stop offset="0" stop-color="var(--hill-herbal-a)"/>
            <stop offset="1" stop-color="var(--hill-herbal-b)"/>
          </linearGradient>
        </defs>
        <path d="M0 88 C30 50 70 25 110 28 C150 32 170 60 200 88 Z" fill="url(#herbal-fill)" stroke="var(--ink)" stroke-width="1.2"/>
      </svg>
      <span class="tea-tag">Herbal Tea</span>
      <span class="tea-weight">50g</span>
    </section>

    <section class="label label--green">
      <div class="label-name">Verdelle</div>
      <svg class="hill" viewBox="0 0 200 90" role="img" aria-label="Sage green striped hill illustration">
        <defs>
          <linearGradient id="green-fill" x1="0" x2="1">
            <stop offset="0" stop-color="var(--hill-green-b)"/>
            <stop offset="1" stop-color="var(--hill-green-a)"/>
          </linearGradient>
        </defs>
        <path d="M0 88 C30 50 70 25 110 28 C150 32 170 60 200 88 Z" fill="url(#green-fill)" stroke="var(--hill-green-a)" stroke-width="1.2"/>
      </svg>
      <span class="tea-tag">Green Tea</span>
      <span class="tea-weight">50g</span>
    </section>

    <section class="label label--black">
      <div class="label-name">Verdelle</div>
      <svg class="hill" viewBox="0 0 200 90" role="img" aria-label="Charcoal striped hill illustration">
        <defs>
          <linearGradient id="black-fill" x1="0" x2="1">
            <stop offset="0" stop-color="var(--hill-black-b)"/>
            <stop offset="1" stop-color="var(--hill-black-a)"/>
          </linearGradient>
        </defs>
        <path d="M0 88 C30 50 70 25 110 28 C150 32 170 60 200 88 Z" fill="url(#black-fill)" stroke="var(--hill-black-a)" stroke-width="1.2"/>
      </svg>
      <span class="tea-tag">Black Tea</span>
      <span class="tea-weight">50g</span>
    </section>
  </main>
</body>
</html>
```